A website for a Maltese Law Firm

Our law firm needs a website to further its business. The site should have a simple yet effective design. We would need the following sections: About us, Practice Areas, About Malta, Contact. These should be further split as follows:

About us: Our firm, Our values, What others say, Offices

Practice Areas: Crimimal, Citizenship & Residence, Harbour Passage Scheme, Criminal Defence, Civil Litigation, Arbitration and ADR, Commercial and Corporate, Media Law.

About Malta: just one section.

Contact: Just one section

We would also need a news feed at the front of the site to include latest news regarding our cases.

At the bottom we need a section for our Terms and a Privacy Statement.

Our logo is being attached.

Target Market(s)

All clients looking for legal assistance in Malta

Industry/Entity Type

Legal

Coding

Coded - Design and coding required

Number of Pages Required

1 page

Requirements
Must have
• It must be simple yet striking.

```html
<!DOCTYPE html>
<html lang="en">
<head>
<meta charset="utf-8">
<title>Dalli &amp; Brincat Advocates</title>
<link href="https://fonts.googleapis.com/css2?family=Cinzel:wght@400;700&family=Raleway:wght@500&family=Roboto+Condensed&family=Crimson+Text&display=swap" rel="stylesheet">
<style>
:root{
  --ink:#1a1a1a;
  --text:#333;
  --muted:#777;
  --rule:#d4d4d4;
  --topbar:#4b4b4b;
  --accent:#e9a04a;
  --accent-dark:#3a2a14;
  --white:#fff;
  --grey-band:#ececec;
  --footer:#1d1d1d;
  --footer-text:#c9c9c9;
}
*{box-sizing:border-box;margin:0;padding:0}
html,body{width:1200px;height:2394px;overflow:hidden}
body{position:relative;background:var(--white);font-family:Arial,Helvetica,sans-serif;color:var(--text)}
.btn{position:absolute;display:flex;align-items:center;justify-content:center;font:bold 13px Arial,sans-serif;color:var(--white);background:var(--ink)}

/* top bar */
.topbar{position:absolute;left:0;top:0;width:1200px;height:35px;background:var(--topbar)}
.social{position:absolute;top:8px;display:flex;gap:13px}
.social span{width:18px;height:18px;border:1px solid #ccc;display:block}
.schedule{position:absolute;left:479px;top:0;width:279px;height:35px;background:var(--accent);color:var(--accent-dark);font:400 15px "Cinzel",serif;display:flex;align-items:center;justify-content:center}
.top-contact{position:absolute;top:0;height:35px;display:flex;align-items:center;gap:10px;color:var(--white);font-size:13px}
.top-contact svg{display:block}

/* header */
.header{position:absolute;left:0;top:35px;width:1200px;height:90px;background:var(--white)}
.firm-name{font-family:"Cinzel",serif;font-weight:400;color:var(--ink);line-height:1.1}
.header .firm-name{position:absolute;left:80px;top:21px;font-size:22px}
.nav{position:absolute;left:396px;top:46px;display:flex;font:400 14px "Cinzel",serif;color:#555}
.nav a{padding:0 12px;border-left:1px solid var(--rule);color:inherit;text-decoration:none;line-height:16px}
.nav a:first-child{border-left:0;color:var(--ink)}

/* hero */
.hero{position:absolute;left:0;top:125px;width:1200px;height:510px;background:linear-gradient(115deg,#3a2313 0%,#8a5226 30%,#c98a45 55%,#7a4520 78%,#2e1b0e 100%)}
.hero-caption{position:absolute;left:80px;top:194px;width:547px;height:136px;background:rgba(0,0,0,.55);padding:14px 14px}
.hero-caption h1{font:500 28px/32px "Raleway",sans-serif;color:var(--white)}
.hero-caption .more{position:absolute;left:14px;top:86px;width:106px;height:30px;background:#ddd;color:var(--ink);font:bold 14px Arial,sans-serif;display:flex;align-items:center;justify-content:center}
.hero-arrow{position:absolute;top:241px;width:28px;height:28px;border-radius:50%;background:var(--ink);display:flex;align-items:center;justify-content:center}

/* about */
.about-title{position:absolute;left:80px;top:686px;font:400 28px/1 "Cinzel",serif;color:var(--ink)}
.about-text{position:absolute;left:80px;top:738px;width:645px;font-size:12px;line-height:20px;color:#444}
.side-list{position:absolute;left:802px;top:688px;width:320px}
.side-item{display:flex;gap:18px;height:86px}
.side-icon{width:40px;height:40px;border:1px solid #999;flex:none}
.side-item h3{font:400 13px "Cinzel",serif;color:var(--ink);margin:-2px 0 4px}
.side-item p{font-size:12px;line-height:18px;color:#444}

/* practice band */
.practice{position:absolute;left:0;top:942px;width:1200px;height:395px;background:linear-gradient(180deg,#2f3038 0%,#4a4138 45%,#3a2c22 100%)}
.practice h2{position:absolute;left:80px;top:22px;width:677px;font:400 28px "Cinzel",serif;color:var(--white);border-bottom:1px solid rgba(255,255,255,.35);padding-bottom:8px}
.areas{position:absolute;left:80px;top:86px;display:grid;grid-template-columns:388px 300px;row-gap:19px}
.area{display:flex;align-items:center;gap:14px;font:18px "Crimson Text",serif;color:var(--white);height:40px}
.area i{width:40px;height:40px;border:1px solid rgba(255,255,255,.8);background:rgba(255,255,255,.08);display:block;flex:none}
.callus{position:absolute;left:78px;top:332px;font:22px "Roboto Condensed",sans-serif;color:var(--white)}
.form-box{position:absolute;left:814px;top:22px;width:303px;height:341px;background:rgba(95,95,95,.65)}
.form-box h3{position:absolute;left:12px;top:12px;width:279px;font:400 20px/23px "Cinzel",serif;color:var(--white);border-bottom:1px solid rgba(255,255,255,.3);padding-bottom:8px}
.field{position:absolute;left:13px;width:277px;height:36px;background:rgba(255,255,255,.28);color:var(--white);font-size:13px;padding:10px 8px}
.field.select::after{content:"V";position:absolute;right:12px;top:10px;font-size:12px}

/* case studies */
.section-title{position:absolute;font:400 28px "Cinzel",serif;color:var(--ink);border-bottom:1px solid var(--rule);padding-bottom:6px}
.pager{position:absolute;display:flex;gap:9px}
.pager span{width:22px;height:20px;border:1px solid var(--ink);display:flex;align-items:center;justify-content:center;background:var(--white)}
.case-photo{position:absolute;top:1448px;width:216px;height:216px}
.case-body{position:absolute;top:1448px;width:262px}
.case-body h4{font:15px/21px Arial,sans-serif;color:var(--ink);border-bottom:1px solid var(--rule);padding-bottom:8px;margin-bottom:10px}
.case-body p{font-size:12.5px;line-height:19px;color:#444}
.case-body .btn{position:static;width:88px;height:30px;margin-top:16px}

/* testimonials */
.testimonials{position:absolute;left:0;top:1711px;width:1200px;height:383px;background:var(--grey-band)}
.avatar{position:absolute;left:124px;top:125px;width:110px;height:110px;border-radius:50%;background:linear-gradient(#c9b8a6,#8e9aa8);border:4px solid var(--white)}
.quote{position:absolute;left:270px;top:128px;width:812px;font:italic 12px/22px Arial,sans-serif;color:#444}
.quote .mark{font:bold 30px/12px Georgia,serif;color:#999;vertical-align:-8px;margin-right:6px}
.quote-by{position:absolute;left:270px;top:250px;font:italic bold 12px Arial,sans-serif;color:var(--ink)}

/* footer */
.footer{position:absolute;left:0;top:2094px;width:1200px;height:300px;background:var(--footer);color:var(--footer-text)}
.follow{position:absolute;left:84px;top:-12px;width:218px;height:38px;background:var(--accent);display:flex;align-items:center;gap:10px;padding-left:20px;color:var(--white);font-size:12px}
.follow span{width:20px;height:20px;border:1px solid var(--white);display:block}
.foot-col h5{font:400 14px "Cinzel",serif;color:var(--white);border-bottom:1px solid #444;padding-bottom:8px;margin-bottom:14px}
.foot-col{position:absolute;top:56px}
.footer .firm-name{color:var(--white);font-size:17px;margin-bottom:16px}
.links li{list-style:none;font-size:12px;line-height:22px;padding-left:18px;position:relative}
.links li::before{content:"";position:absolute;left:0;top:10px;width:4px;height:1px;background:#888}
.contact-row{display:flex;gap:10px;font-size:12px;line-height:17px;margin-bottom:12px;color:var(--white)}
.contact-row svg{flex:none}
.map{position:absolute;left:589px;top:60px;width:261px;height:169px;background:linear-gradient(135deg,#d9d8c8,#c7d2b8 50%,#a9c3dd);border:3px solid #555}
.hours-row{display:flex;justify-content:space-between;font-size:12px;line-height:34px}
.copyright{position:absolute;left:0;top:273px;width:1200px;display:flex;align-items:center;gap:14px;font-size:12px;color:var(--footer-text)}
.copyright .rule{flex:1;height:1px;background:#666}
.footer-strip{position:absolute;left:0;top:290px;width:1200px;height:10px;background:#444}
</style>
</head>
<body>

<!-- top bar -->
<div class="topbar">
  <div class="social" style="left:80px"><span></span><span></span><span></span><span></span></div>
  <div class="schedule">Schedule Free Consultation</div>
  <div class="top-contact" style="left:770px">
    <svg width="20" height="20" viewBox="0 0 20 20"><rect width="20" height="20" fill="#fff"/><path d="M6 4l2 3-1.5 1.5a8 8 0 004 4L12 11l3 2-1 2.5C9 15 5 11 4.5 6z" fill="#4b4b4b"/></svg>
    <span>356 2000 4821</span>
  </div>
  <div class="top-contact" style="left:910px">
    <svg width="22" height="18" viewBox="0 0 22 18"><rect width="22" height="18" fill="#fff"/><path d="M4 5h14v9H4z" fill="none" stroke="#4b4b4b" stroke-width="1.5"/><path d="M4 5l7 5 7-5" fill="none" stroke="#4b4b4b" stroke-width="1.5"/></svg>
    <span>info@dbadvocates.example</span>
  </div>
</div>

<!-- header -->
<header class="header">
  <div class="firm-name">Dalli &amp; Brincat<br>Advocates</div>
  <nav class="nav">
    <a>Home</a><a>About Us</a><a>Our Firm</a><a>Our Values</a><a>What Others Say</a><a>Offices</a><a>Contact Us</a>
  </nav>
</header>

<!-- hero -->
<section class="hero" role="img" aria-label="Judge's gavel, law books and handcuffs on a wooden desk in warm light">
  <div class="hero-arrow" style="left:36px"><svg width="10" height="10" viewBox="0 0 10 10"><path d="M7 1L3 5l4 4" stroke="#fff" stroke-width="2" fill="none"/></svg></div>
  <div class="hero-arrow" style="left:1134px"><svg width="10" height="10" viewBox="0 0 10 10"><path d="M3 1l4 4-4 4" stroke="#fff" stroke-width="2" fill="none"/></svg></div>
  <div class="hero-caption">
    <h1>Get Qualified Legal Advice Against Criminal Act Law</h1>
    <span class="more">Read More</span>
  </div>
</section>

<!-- about -->
<h2 class="about-title">About Dalli &amp; Brincat</h2>
<p class="about-text">Lorem ipsum dolor sit amet, consectetuer adipiscing elit, sed diam nonummy nibh euismod tincidunt ut laoreet lore dolore magna aliquam erat volutpat. Ut wisi enim ad minim veniam, quis nostrud exerci tation ullamcorper suscipit lobortisser nisl ut aliquip ex ea commodo consequat. Duis autem vel eum iriure dolor in hendrerit in vulputate velit lore,sdfesse molestie consequat, vel illum dolore eu feugiat nulla facilisis at vloboriis nisl ut aliquip ex ea commodo consequat. erereererereDuis autem vel eum iriure dolor in hendrerit in vulputate velit ero eros et accumsan et iusto odio dignissim qui blandit praesent luptatum zzril delenit augue duis dolore te feugait nulla facilisi.</p>
<div class="btn" style="left:80px;top:874px;width:104px;height:28px">Read More</div>

<div class="side-list">
  <div class="side-item"><div class="side-icon" role="img" aria-label="Scales icon"></div><div><h3>Our Firm</h3><p>Lorem ipsum dolor sit amet, consectetuer adipiscing elit, sed dianonummy nibh</p></div></div>
  <div class="side-item"><div class="side-icon" role="img" aria-label="Handshake icon"></div><div><h3>Our Values</h3><p>Lorem ipsum dolor sit amet, consectetuer adipiscing elit, sed dianonum</p></div></div>
  <div class="side-item"><div class="side-icon" role="img" aria-label="City buildings icon"></div><div><h3>About Malta City</h3><p>Lorem ipsum dolor sit amet, consectetuer adi elit, sed dianonummy nibh euismod</p></div></div>
</div>

<!-- practice areas -->
<section class="practice" role="img" aria-label="Dusk view of Valletta rooftops and church dome, darkened">
  <h2>Our Practice Areas</h2>
  <div class="areas">
    <div class="area"><i></i>Criminal Law</div>
    <div class="area"><i></i>Criminal Defence</div>
    <div class="area"><i></i>Citizenship &amp; Residence</div>
    <div class="area"><i></i>Civil Litigation</div>
    <div class="area"><i></i>Harbour Passage Scheme</div>
    <div class="area"><i></i>Arbitration &amp; ADR</div>
    <div class="area"><i></i>Commercial &amp; Corporate</div>
    <div class="area"><i></i>Media Law</div>
  </div>
  <p class="callus">Call us 356 2000 4821&nbsp; at&nbsp; or contact us online for a Free estimate</p>
  <div class="form-box">
    <h3>Request for Free Consulatation</h3>
    <div class="field" style="top:74px">Name</div>
    <div class="field" style="top:118px">Email</div>
    <div class="field select" style="top:162px">Inquiry Tpye</div>
    <div class="field" style="top:208px;height:62px">Message</div>
    <div class="btn" style="left:14px;top:284px;width:104px;height:28px">SUBMIT</div>
  </div>
</section>

<!-- recent case studies -->
<h2 class="section-title" style="left:80px;top:1380px;width:325px">Recent Case Studies</h2>
<div class="pager" style="left:1066px;top:1391px">
  <span><svg width="8" height="10" viewBox="0 0 8 10"><path d="M6 1L2 5l4 4" stroke="#1a1a1a" stroke-width="1.5" fill="none"/></svg></span>
  <span><svg width="8" height="10" viewBox="0 0 8 10"><path d="M2 1l4 4-4 4" stroke="#1a1a1a" stroke-width="2" fill="none"/></svg></span>
</div>

<div class="case-photo" style="left:80px;background:linear-gradient(160deg,#5a3a22,#b07a44 60%,#6a4a2e)" role="img" aria-label="Two lawyers at a meeting table in a library"></div>
<div class="case-body" style="left:316px">
  <h4>Ut wisi enim ad minim veniam quis nostrud exerci tation</h4>
  <p>Lorem ipsum dolor sit amet, consectetuer adipiscing elit, seadipiscing elit, ssed diam nonummy nibh euismod tincidunt ut laoreet dolore magna d diam nonummy nloreeribh euismod tincidunt ut laoreet dolore magna aliquam erat volutpat.</p>
  <div class="btn">Read More</div>
</div>

<div class="case-photo" style="left:620px;background:linear-gradient(160deg,#d8d8d8,#8a8a8a 55%,#3a3a3a)" role="img" aria-label="Lawyer working at a desk beside a statue of justice"></div>
<div class="case-body" style="left:860px">
  <h4>Ut wisi enim ad minim veniam quis nostrud exerci tation</h4>
  <p>Lorem ipsum dolor sit amet, consectetuer adipiscing elit, seadipiscing elit, ssed diam nonummy nibh euismod tincidunt ut laoreet dolore magna d diam nonummy nloreeribh euismod tincidunt ut laoreet dolore magna aliquam erat volutpat.</p>
  <div class="btn">Read More</div>
</div>

<!-- testimonials -->
<section class="testimonials">
  <h2 class="section-title" style="left:392px;top:58px;width:420px;text-align:center">What Other's Say About Us</h2>
  <div class="avatar" role="img" aria-label="Client portrait"></div>
  <p class="quote"><span class="mark">&ldquo;</span>Lorem ipsum dolor sit amet, consectetuer adipiscing elit, sed diam nonummy nibh euismod tincidunt ut laoreet dolore magna aliquam erat volutpat. Ut wisi enim ad minim veniam, quis nostrud exerci tation ullamcorper suscipit lobortis nisl ut aliquip commodo consequat. Duis autem vel eum iriure dolor in hendrerit in vulputate velit esse molestie consequat, vel illum dolore eu feugiat nulla facilisis at vero eros et accumsan et iusto odio dignissimaugue duis dolore te feugait nulla facilisi.</p>
  <p class="quote-by">.... Lorem Ispum, Manger</p>
  <div class="pager" style="left:574px;top:300px">
    <span><svg width="8" height="10" viewBox="0 0 8 10"><path d="M6 1L2 5l4 4" stroke="#1a1a1a" stroke-width="1.5" fill="none"/></svg></span>
    <span><svg width="8" height="10" viewBox="0 0 8 10"><path d="M2 1l4 4-4 4" stroke="#1a1a1a" stroke-width="2" fill="none"/></svg></span>
  </div>
</section>

<!-- footer -->
<footer class="footer">
  <div class="follow">Follow us <span></span><span></span><span></span><span></span></div>

  <div class="foot-col" style="left:84px;width:190px">
    <h5>Quick Links</h5>
    <ul class="links">
      <li>Home</li><li>About Us</li><li>Our Firm</li><li>Our Values</li><li>What Others Say</li><li>Offices</li><li>Contact Us</li>
    </ul>
  </div>

  <div class="foot-col" style="left:310px;width:236px">
    <h5>Contact Details</h5>
    <div class="contact-row"><svg width="16" height="16" viewBox="0 0 16 16"><rect width="16" height="16" fill="#fff"/><path d="M8 3a3 3 0 00-3 3c0 2.5 3 6 3 6s3-3.5 3-6a3 3 0 00-3-3z" fill="#1d1d1d"/></svg><span>12/4, Old Bakery Lane, Valletta<br>88, Mill Road, Birkirkara</span></div>
    <div class="contact-row"><svg width="16" height="16" viewBox="0 0 16 16"><rect width="16" height="16" fill="#fff"/><path d="M5 3l1.5 2.5-1 1a6 6 0 003 3l1-1L12 10l-.8 2C7 12 4 9 3.8 4.8z" fill="#1d1d1d"/></svg><span>356 2000 4821 ( Valletta )</span></div>
    <div class="contact-row"><svg width="16" height="16" viewBox="0 0 16 16"><rect width="16" height="16" fill="#fff"/><path d="M5 3l1.5 2.5-1 1a6 6 0 003 3l1-1L12 10l-.8 2C7 12 4 9 3.8 4.8z" fill="#1d1d1d"/></svg><span>356 2000 4822 (Birkirkara )</span></div>
    <div class="contact-row"><svg width="16" height="16" viewBox="0 0 16 16"><rect width="16" height="16" fill="#fff"/><path d="M3 5h10v7H3zM3 5l5 4 5-4" fill="none" stroke="#1d1d1d" stroke-width="1.2"/></svg><span>info@dbadvocates.example</span></div>
  </div>

  <div class="map" role="img" aria-label="Map of Malta showing office locations"></div>

  <div class="foot-col" style="left:892px;top:12px;width:210px">
    <div class="firm-name">Dalli &amp; Brincat<br>Advocates</div>
    <h5>Meeting Hours</h5>
    <p style="font-size:12px;line-height:18px;margin-bottom:4px">Lorem ispum is the dummy text of the industry&nbsp; lorem fds fdurei.</p>
    <div class="hours-row"><span>Monday-Friday:</span><span>9am to 5pm</span></div>
    <div class="hours-row"><span>Saturday:</span><span>10am to 2pm</span></div>
    <div class="hours-row"><span>Sunday:</span><span>Clised</span></div>
  </div>

  <div class="copyright"><span class="rule"></span><span>Copyright &copy; 2016 Dalli &amp; Brincat Advocates. All Rights Reserved.&nbsp; Disclaimer</span><span class="rule"></span></div>
  <div class="footer-strip"></div>
</footer>

</body>
</html>
```